Website design and Setup for Real Estate Firm and Going Live

We are a commercial real estate investment firm and are looking for a 6 page website which is informational only. Some text and graphics on each page. We would want the designer to code and launch the website. This website needs to be corporate looking as well as innovative. We are setting up the website on hostivo.

The first page will be a home page with generic commercial real estate look with a link to the following 5 pages on page 1. So page one (the Home Page should have a commercial real estate look with the text linking to the following pages. Page 2 "About Us" with 3 paragraphs describing our firm. Page 3 "Our Platform" with another few paragraphs on due diligence, acquisitions, financing, and management.

Page 4 is "Our Team" highlighting several manager profiles. Page 5 is our "investment Portfolio portal" which will be password protected so not a lot of text, only general graphics and anyone viewing the site casually won't get into the backend, Page 6 is the contact us page. All of the content will be uploaded shortly.

The project includes setting up hyperlinks in the website as well rotating images etc and a final complete live online product. We do not expect to pay for any stock images.

Target Market(s)

Investors, Real Estate Professionals, Brokerages

Industry/Entity Type

Real Estate

Coding

Coded - Design and coding required

Number of Pages Required

5+ page

Requirements
Must have
• Corporate cutting edge design, suitable for a financial corporation.

```html
<!DOCTYPE html>
<html lang="en">
<head>
<meta charset="utf-8">
<title>Dean Marlow Realty</title>
<link href="https://fonts.googleapis.com/css2?family=Raleway:wght@600;700&family=Work+Sans:wght@400;500;600&display=swap" rel="stylesheet">
<style>
:root{
  --gold:#b08e1a;
  --gold-soft:#c7a62e;
  --ink:#1c1c1c;
  --text:#4a4a4a;
  --muted:#eceef2;
  --white:#ffffff;
  --line:#d6d6d6;
}
*{margin:0;padding:0;box-sizing:border-box}
html,body{width:1200px;height:4170px;overflow:hidden}
body{position:relative;background:var(--white);font-family:"Work Sans",sans-serif;color:var(--text)}
.abs{position:absolute}
h1,h2,h3,.brand{font-family:"Raleway",sans-serif}
.accent{color:var(--gold)}
.btn{position:absolute;background:var(--gold);color:var(--white);font:600 14px "Work Sans",sans-serif;letter-spacing:.5px;display:flex;align-items:center;justify-content:center;text-transform:uppercase}
.btn.framed::after{content:"";position:absolute;left:8px;top:8px;right:-8px;bottom:-8px;border:2px solid var(--ink);z-index:-1}
.brand-mark{display:flex;align-items:center;gap:14px;color:var(--white);font-weight:600;font-size:19px;line-height:1.25}
.brand-mark .dot{width:40px;height:40px;border:3px solid var(--white);border-radius:50%}

/* hero */
.hero-photo{left:0;top:0;width:1200px;height:720px}
.nav{top:40px;left:520px;display:flex;gap:28px;font:600 13px "Work Sans",sans-serif;color:var(--white)}
.nav .active{color:var(--gold-soft)}
.hero-box{left:296px;top:259px;width:608px;height:190px;background:rgba(255,255,255,.78);text-align:center;padding-top:30px}
.hero-box h1{font-size:38px;color:var(--ink);font-weight:700}
.hero-box p{font-size:18px;color:var(--ink);font-weight:500;margin-top:8px;line-height:1.45}
.emblem{width:72px;height:72px;border-radius:50%;background:var(--white);box-shadow:0 2px 10px rgba(0,0,0,.25);border:4px solid var(--gold)}

/* sections */
.sec-title{font-size:34px;font-weight:700;color:var(--ink)}
.copy{font-size:14px;line-height:27px;text-align:justify;color:var(--text)}
.copy p+p{margin-top:18px}
.dots{background-image:radial-gradient(#8a8a8a 1.6px,transparent 1.8px);background-size:10px 10px}

.how{left:0;top:1347px;width:1200px;height:553px;background:linear-gradient(135deg,#f1f2f5,#e4e7ec 50%,#f3f4f7)}
.card{position:absolute;top:1503px;width:229px;height:327px;background:var(--white);box-shadow:0 2px 8px rgba(0,0,0,.1);text-align:center}
.card svg{margin-top:35px}
.card h3{font-size:18px;color:var(--ink);margin-top:24px;letter-spacing:.5px}
.card p{font-size:14px;line-height:24px;margin:14px 12px 0}

.insights{left:0;top:2595px;width:1200px;height:637px;background:linear-gradient(120deg,#b4921c,#a88a22 45%,#b8991f)}
.post{position:absolute;top:2748px;width:308px;height:405px;background:var(--white);text-align:center}
.post .pic{margin:7px;height:192px}
.post .date{font-size:13px;margin-top:18px;color:var(--text)}
.post h3{font-size:17px;color:var(--ink);margin-top:10px}
.post p{font-size:14px;line-height:23px;margin:10px 8px 0}
.post .more{display:inline-block;margin-top:12px;font:600 13px "Work Sans",sans-serif;color:var(--gold);border-bottom:2px solid var(--gold)}

.field{position:absolute;border:1px solid var(--line);background:var(--white);font-size:14px;color:#555;padding:14px 15px}

.footer-nav{top:3978px;left:0;width:1200px;display:flex;justify-content:center;gap:34px;color:var(--white);font:600 17px "Work Sans",sans-serif}
.footer-info{top:4020px;left:0;width:1200px;text-align:center;color:var(--white);font-size:15px}
.social{top:4052px;left:532px;display:flex;gap:8px}
.social span{width:28px;height:28px;border-radius:50%;background:#3a3a3a}
.social span:first-child{background:var(--gold)}
.copyright{top:4130px;left:0;width:1200px;text-align:center;color:var(--white);font-size:13px}
</style>
</head>
<body>

<!-- hero -->
<div class="abs hero-photo" role="img" aria-label="City skyline at dusk with glass towers and light-trailed highways" style="background:linear-gradient(180deg,#2d3c55 0%,#6b6f80 35%,#c7885e 55%,#3c3d4a 80%,#1e2230 100%)"></div>
<svg class="abs" style="left:0;top:500px" width="1200" height="240" viewBox="0 0 1200 240">
  <polygon points="0,18 600,212 1200,18 1200,240 0,240" fill="var(--gold)"/>
  <polygon points="0,30 600,224 1200,30 1200,240 0,240" fill="var(--white)"/>
</svg>
<div class="abs brand-mark" style="left:110px;top:24px"><span class="dot"></span><span class="brand">DEAN MARLOW<br>REALTY</span></div>
<nav class="abs nav"><span class="active">HOME</span><span>ABOUT</span><span>OUR APPROACH</span><span>LEADERSHIP</span><span>INSIGHTS</span><span>CONTACT</span></nav>
<div class="abs hero-box">
  <h1>DEAN MARLOW REALTY</h1>
  <p>Sed ut perspiciatis unde omnis iste natus error sit<br>volupta tem laudantium totam.</p>
</div>
<div class="btn" style="left:525px;top:426px;width:150px;height:50px">Get Started</div>
<div class="abs emblem" style="left:564px;top:650px"></div>

<!-- about -->
<div class="abs dots" style="left:110px;top:770px;width:130px;height:140px"></div>
<div class="abs dots" style="left:378px;top:1110px;width:130px;height:144px"></div>
<div class="abs" style="left:142px;top:802px;width:332px;height:416px;background:var(--white);box-shadow:0 1px 6px rgba(0,0,0,.2)"></div>
<div class="abs" role="img" aria-label="Portrait of the firm's principal in a navy suit" style="left:152px;top:812px;width:312px;height:396px;background:linear-gradient(160deg,#3c5a86,#233656 60%,#1b2a44)"></div>
<h2 class="abs sec-title" style="left:600px;top:812px">ABOUT <span class="accent">DEAN MARLOW REALTY</span></h2>
<div class="abs copy" style="left:600px;top:878px;width:488px">
  <p>Sed ut perspiciatis unde omnis iste natus error sit voluptatem accusantium doloremque laudantium, totam rem aperiam, eaque ipsa quae ab illo inventore veritatis et quasi architecto beatae vitae dicta sunt explicabo. Nemo enim ipsam voluptatem quia voluptas sit aspernatur aut odit aut fugit sed quia.</p>
  <p>At vero eos et accusamus et iusto odio dignissimos ducimus qui blanditiis praesentium voluptatum deleniti atque corrupti quos dolores et quas molestias excepturi.</p>
</div>
<div class="btn framed" style="left:600px;top:1148px;width:154px;height:50px">Leran More</div>

<!-- how it works -->
<div class="abs how"></div>
<h2 class="abs sec-title" style="left:0;width:1200px;text-align:center;top:1408px">HOW IT <span class="accent">WORKS</span></h2>
<div class="card" style="left:112px">
  <svg width="84" height="96" viewBox="0 0 84 96"><polygon points="42,0 84,24 84,72 42,96 0,72 0,24" fill="var(--ink)"/><rect x="32" y="28" width="16" height="40" fill="none" stroke="#fff" stroke-width="2"/><rect x="48" y="44" width="10" height="24" fill="none" stroke="#fff" stroke-width="2"/></svg>
  <h3>OWNER</h3><p>At vero eos et accusamus et iusto odio dignissimos duci mus qui blanditiis pra ese ntium volupta.</p>
</div>
<div class="card" style="left:361px">
  <svg width="84" height="96" viewBox="0 0 84 96"><polygon points="42,0 84,24 84,72 42,96 0,72 0,24" fill="var(--ink)"/><rect x="24" y="30" width="18" height="36" fill="none" stroke="#fff" stroke-width="2"/><rect x="42" y="44" width="18" height="22" fill="none" stroke="#fff" stroke-width="2"/></svg>
  <h3>DEVELOPER</h3><p>At vero eos et accusamus et iusto odio dignissimos duci mus qui blanditiis pra ese ntium volupta.</p>
</div>
<div class="card" style="left:610px">
  <svg width="84" height="96" viewBox="0 0 84 96"><polygon points="42,0 84,24 84,72 42,96 0,72 0,24" fill="var(--gold)"/><circle cx="42" cy="36" r="7" fill="none" stroke="#fff" stroke-width="2"/><path d="M24 66h36M42 43v10M28 53h28v13M28 53v13" fill="none" stroke="#fff" stroke-width="2"/></svg>
  <h3>INVESTOR</h3><p>At vero eos et accusamus et iusto odio dignissimos duci mus qui blanditiis pra ese ntium volupta.</p>
</div>
<div class="card" style="left:859px">
  <svg width="84" height="96" viewBox="0 0 84 96"><polygon points="42,0 84,24 84,72 42,96 0,72 0,24" fill="var(--ink)"/><circle cx="36" cy="40" r="9" fill="none" stroke="#fff" stroke-width="2"/><circle cx="50" cy="58" r="8" fill="none" stroke="#fff" stroke-width="2"/></svg>
  <h3>OPERATOR</h3><p>At vero eos et accusamus et iusto odio dignissimos duci mus qui blanditiis pra ese ntium volupta.</p>
</div>

<!-- approach -->
<h2 class="abs sec-title" style="left:112px;top:2043px">OUR <span class="accent">APPROACH</span></h2>
<div class="abs copy" style="left:112px;top:2110px;width:488px">
  <p>Sed ut perspiciatis unde omnis iste natus error sit voluptatem accusantium doloremque laudantium, totam rem aperiam, eaque ipsa quae ab illo inventore veritatis et quasi architecto beatae vitae dicta sunt explicabo. Nemo enim ipsam voluptatem quia voluptas sit aspernatur aut odit aut fugit sed quia.</p>
  <p>At vero eos et accusamus et iusto odio dignissimos ducimus qui blanditiis praesentium voluptatum deleniti atque corrupti quos dolores et quas molestias excepturi.</p>
</div>
<div class="btn framed" style="left:112px;top:2380px;width:154px;height:50px">Leran More</div>
<svg class="abs" style="left:666px;top:1988px" width="426" height="512" viewBox="0 0 426 512" role="img" aria-label="Business handshake across an office desk">
  <defs><linearGradient id="meeting" x1="0" y1="0" x2="1" y2="1"><stop offset="0" stop-color="#e9e6df"/><stop offset=".55" stop-color="#c8bfb0"/><stop offset="1" stop-color="#7a6c5a"/></linearGradient></defs>
  <polygon points="213,2 424,130 424,382 213,510 2,382 2,130" fill="#fff" stroke="#ddd" stroke-width="2"/>
  <polygon points="213,12 414,135 414,377 213,500 12,377 12,135" fill="url(#meeting)"/>
</svg>

<!-- insights -->
<div class="abs insights" role="img" aria-label="Gold-toned background of business people in an office"></div>
<h2 class="abs sec-title" style="left:0;width:1200px;text-align:center;top:2662px;color:var(--white)">LATEST INSIGHTS</h2>
<div class="post" style="left:112px">
  <div class="pic" role="img" aria-label="Colleagues shaking hands in an office" style="background:linear-gradient(135deg,#b9bcc0,#6f7378)"></div>
  <div class="date"><span class="accent">▦</span> 24 Dec 2021</div>
  <h3>SED UT PERSPICIATIS UNDE</h3>
  <p>Lorem ipsum dolor sit amet, consectetur adipiscing elit, sed do eiusmod tempor incididunt ut labore.</p>
  <span class="more">READ MORE</span>
</div>
<div class="post" style="left:446px">
  <div class="pic" role="img" aria-label="Modern glass office building under blue sky" style="background:linear-gradient(180deg,#5d8fcf,#9fb9d6 45%,#4d5a52)"></div>
  <div class="date"><span class="accent">▦</span> 24 Dec 2021</div>
  <h3>SED UT PERSPICIATIS UNDE</h3>
  <p>Lorem ipsum dolor sit amet, consectetur adipiscing elit, sed do eiusmod tempor incididunt ut labore.</p>
  <span class="more">READ MORE</span>
</div>
<div class="post" style="left:780px">
  <div class="pic" role="img" aria-label="Two agents reviewing documents outside an apartment block" style="background:linear-gradient(135deg,#3b3b3d,#8c8a86 60%,#d9d6d0)"></div>
  <div class="date"><span class="accent">▦</span> 24 Dec 2021</div>
  <h3>SED UT PERSPICIATIS UNDE</h3>
  <p>Lorem ipsum dolor sit amet, consectetur adipiscing elit, sed do eiusmod tempor incididunt ut labore.</p>
  <span class="more">READ MORE</span>
</div>

<!-- contact -->
<div class="abs" role="img" aria-label="Faded grey city skyline" style="left:0;top:3440px;width:1200px;height:520px;background:linear-gradient(180deg,#ffffff,#d9d9d9 60%,#bdbdbd)"></div>
<h2 class="abs sec-title" style="left:0;width:1200px;text-align:center;top:3320px">CONTACT <span class="accent">US</span></h2>
<div class="field" style="left:210px;top:3405px;width:386px;height:46px">First Name</div>
<div class="field" style="left:604px;top:3405px;width:386px;height:46px">Last Name</div>
<div class="field" style="left:210px;top:3461px;width:386px;height:46px">Phone Number</div>
<div class="field" style="left:604px;top:3461px;width:386px;height:46px">Email Address</div>
<div class="field" style="left:210px;top:3517px;width:780px;height:82px">Comment</div>
<div class="btn" style="left:510px;top:3614px;width:180px;height:48px">Send Message</div>

<!-- footer -->
<svg class="abs" style="left:0;top:3750px" width="1200" height="420" viewBox="0 0 1200 420">
  <polygon points="0,180 600,14 1200,180 1200,420 0,420" fill="var(--gold)"/>
  <polygon points="0,196 600,30 1200,196 1200,420 0,420" fill="#151515"/>
</svg>
<div class="abs emblem" style="left:564px;top:3730px"></div>
<div class="abs brand-mark" style="left:488px;top:3880px;font-size:21px"><span class="dot" style="border-color:var(--gold)"></span><span class="brand">DEAN MARLOW<br>REALTY</span></div>
<nav class="abs footer-nav"><span>HOME</span><span>ABOUT</span><span>OUR APPROACH</span><span>LEADERSHIP</span><span>INSIGHTS</span><span>CONTACT</span></nav>
<div class="abs footer-info"><span class="accent">✆</span>&nbsp; 555 - 210 - 4836 &nbsp;&nbsp; | &nbsp;&nbsp;<span class="accent">⬤</span>&nbsp; 88 Harbor Point Avenue, United States</div>
<div class="abs social"><span></span><span></span><span></span><span></span></div>
<div class="abs" style="left:112px;top:4112px;width:976px;height:1px;background:#444"></div>
<div class="abs copyright">© 2021 <b>DEAN MARLOW REALTY</b>. All Rights Reserved</div>

</body>
</html>
```